Design some Business Cards for Varnok Advisory

A new business card design - scope

2 sides
Side 1 - varnok logo & add what you think might be good
Side 2 - name address etc & varnok logo. Use logos for twitter if you want

Name - Gideon Marsh
Position - Managing Director
Address - Level 5, 27 Harrow Lane, Melbourne, VIC 3000
Tel - +61 3 9555 0187
Mob - +61 491 570 236
Email - gmarsh@varnok.com.au
Web - www.varnok.com.au
Twitter - twitter.com/varnokadvise
LinkedIn - au.linkedin.com/in/gideon

Font for name etc - Rockwell

Colours

Blue -Cyan 96%, Magenta 66%, Yellow 8%, Black 30%

Grey - Cyan 55%, Magenta 46%, Yellow 42%, Black 2%

Current card is Varnok Biz card Front & Back v2.0

Logos are attached - up to you to use blue or white varnok logo.

```html
<!DOCTYPE html>
<html lang="en">
<head>
<meta charset="utf-8">
<title>Varnok Advisory – Business Cards</title>
<link href="https://fonts.googleapis.com/css2?family=Lato:wght@400;700&display=swap" rel="stylesheet">
<style>
  :root {
    --brand-blue: #1d4687;
    --brand-blue-dark: #163a72;
    --text-grey: #5f6368;
    --rule-grey: #a9abad;
    --card-white: #f7f7f6;
    --page-bg: #e9e8e5;
    --on-blue: #ffffff;
  }
  * { box-sizing: border-box; margin: 0; padding: 0; }
  html, body {
    width: 1200px; height: 895px; overflow: hidden;
    background: var(--page-bg);
    font-family: "Lato", "Helvetica Neue", Arial, sans-serif;
  }
  .sheet {
    width: 1200px; height: 895px;
    display: flex; flex-direction: column; align-items: center; justify-content: center; gap: 48px;
  }
  .card {
    position: relative;
    width: 660px; height: 377px;
    border-radius: 4px;
    box-shadow: 0 2px 10px rgba(0,0,0,.12);
  }
  /* Company name block */
  .company {
    display: flex; align-items: center; gap: 12px;
    font-size: 30px; font-weight: 400; line-height: 1;
  }
  .company__mark { width: 18px; height: 18px; background: currentColor; flex: none; }

  /* Front: contact side */
  .card--front { background: var(--card-white); color: var(--text-grey); }
  .card--front .company { position: absolute; left: 48px; top: 78px; color: var(--brand-blue); }
  .rule {
    position: absolute; left: 48px; right: 48px; top: 140px;
    height: 1px; background: var(--rule-grey);
  }
  .person { position: absolute; left: 48px; top: 160px; }
  .person__name { font-size: 21px; font-weight: 700; color: var(--text-grey); }
  .person__role { font-size: 13px; letter-spacing: 1.2px; color: var(--brand-blue); margin-top: 3px; }
  .contact { position: absolute; left: 48px; top: 218px; list-style: none; font-size: 13.5px; line-height: 22px; }
  .contact li { display: flex; align-items: center; gap: 10px; }
  .contact svg { width: 13px; height: 13px; flex: none; }
  .social { position: absolute; right: 48px; top: 160px; list-style: none; font-size: 13.5px; line-height: 22px; }
  .social li { display: flex; align-items: center; gap: 9px; }
  .social .dot { width: 9px; height: 9px; background: var(--text-grey); border-radius: 2px; }
  .address {
    position: absolute; left: 48px; right: 48px; bottom: 30px;
    font-size: 13.5px; text-align: right;
  }

  /* Back: brand side */
  .card--back { background: var(--brand-blue); color: var(--on-blue); display: flex; align-items: center; justify-content: center; }
  .card--back::after {
    content: ""; position: absolute; inset: auto 0 0 0; height: 6px;
    background: var(--brand-blue-dark); border-radius: 0 0 4px 4px;
  }
  .card--back .company { font-size: 36px; }
  .card--back .company__mark { width: 22px; height: 22px; }
</style>
</head>
<body>
<main class="sheet">
  <section class="card card--front" aria-label="Card front">
    <div class="company"><span class="company__mark"></span>Varnok Advisory</div>
    <div class="rule"></div>
    <div class="person">
      <div class="person__name">Gideon Marsh</div>
      <div class="person__role">MANAGING DIRECTOR</div>
    </div>
    <ul class="contact">
      <li><svg viewBox="0 0 16 16"><path d="M4 1l3 3-2 2c1 2 3 4 5 5l2-2 3 3-2 3C7 15 1 9 1 3z" fill="#5f6368"/></svg>+61 3 9555 0187</li>
      <li><svg viewBox="0 0 16 16"><rect x="4" y="1" width="8" height="14" rx="1.5" fill="none" stroke="#5f6368" stroke-width="1.6"/><circle cx="8" cy="12.5" r="1" fill="#5f6368"/></svg>+61 491 570 236</li>
      <li><svg viewBox="0 0 16 16"><rect x="1" y="3" width="14" height="10" fill="none" stroke="#5f6368" stroke-width="1.6"/><path d="M1 3l7 6 7-6" fill="none" stroke="#5f6368" stroke-width="1.6"/></svg>gmarsh@varnok.com.au</li>
      <li><svg viewBox="0 0 16 16"><rect x="1" y="2" width="14" height="10" fill="none" stroke="#5f6368" stroke-width="1.6"/><path d="M5 15h6M8 12v3" stroke="#5f6368" stroke-width="1.6"/></svg>www.varnok.com.au</li>
    </ul>
    <ul class="social">
      <li><span class="dot"></span>@varnokadvise</li>
      <li><span class="dot"></span>gideon</li>
    </ul>
    <p class="address">Level 5, 27 Harrow Lane, Melbourne, VIC 3000</p>
  </section>

  <section class="card card--back" aria-label="Card back">
    <div class="company"><span class="company__mark"></span>Varnok Advisory</div>
  </section>
</main>
</body>
</html>
```